Visual Storytelling for Calvero’s Next-Gen Product Launch: Crafting a High-Impact Infographic

We are launching a new product called Calvero, under our brand Moltek. This is an indoor/outdoor adhesive for kitchens, bathrooms, water features, pools, countertops, backsplashes, etc. We are launching the product at a tradeshow in January. We like the tag line; bold work, bright build, pure Calvero.
This is a pretty innovative product, nothing like it on the market in terms of performance, UV stability, application, bond strength and color match to substrates. We are looking for infographics that capture the key features and benefits that set this product apart from the competition.
The slide show I provided was the information to use on the design info graphic. The most important information is captured on slides 2-4 (which you have). I would like info graphic capturing some/all/variations of that information to use on marketings slicks, merch, web, app, digital copy, etc.

Target Market(s)

Industry professionals and decision-makers who need a quick, visual understanding of the value proposition. This would include distributors and their customers, fabrication shops in the construction field.

Industry/Entity Type

Distributors and Construction field- Fabricators/ Stone Shops for indoor/outdoor kitchens, baths, water features, wall paneling, bars, restaurants, etc.

Font styles to use
Serif
Sans Serif

Colors
F0912C
F2A743
F7CA91
FBE8D2
FDF5EE
EE7325
F08F49
F5BC92
FAE3D3
FDF4ED

Requirements
Must have
• Clear visual explanation of the new product’s purpose, key features, and benefits Branded design aligned with Calvero’s visual identity (colors, fonts, tone) Sections for: Product overview Core features / differentiators Customer pain points solved Key stats, metrics, or performance highlights Launch date or availability info (if applicable) High-resolution, print- and digital-ready deliverables (PNG + PDF + source file) Modern, clean, and professional infographic layout Icons, illustrations, or minimal visuals that support clarity
Nice to have
• A subtle narrative arc (problem → solution → value → impact) Light animation-ready design elements (for future motion graphics) Optional comparison panel (e.g., “How Calvero differs from existing solutions”) Whitespace-balanced layout for easy reading Optional stylized timeline or flowchart Version variations for social media aspect ratios
Should not have
• Overly busy graphics or cluttered layouts Loud, off-brand colors or cartoonish styles Generic stock imagery that distracts from the product story Long paragraphs—this should be visual-first, not text-heavy Proprietary or confidential data baked into the design (unless provided intentionally) Inconsistent icon styles or mixed illustration aesthetics

```html
<!DOCTYPE html>
<html lang="en">
<head>
<meta charset="utf-8">
<title>Calvero by Moltek — Launch Infographic</title>
<link rel="stylesheet" href="https://fonts.googleapis.com/css2?family=Montserrat:wght@400;500;600;700&family=Libre+Baskerville:ital@1&display=swap">
<style>
  :root {
    --bg: #f7f2e6;
    --ink: #2b2622;
    --ink-soft: #3b342e;
    --brand: #ee7325;
    --brand-deep: #c2621f;
    --brand-dark: #a9501a;
    --amber: #f0912c;
    --peach: #f7ca91;
    --peach-soft: #f5bc92;
    --panel: #f6e7d0;
    --panel-light: #fbeedd;
    --line: #d3782f;
    --pill: #2e2a26;
  }
  * { box-sizing: border-box; margin: 0; padding: 0; }
  html, body { width: 1200px; height: 1200px; overflow: hidden; }
  body {
    background: var(--bg);
    font-family: "Montserrat", Arial, sans-serif;
    color: var(--ink);
    position: relative;
  }

  .masthead { position: absolute; top: 66px; left: 0; width: 1200px; text-align: center; }
  .brand-name {
    font-weight: 600; font-size: 50px; letter-spacing: 1px; line-height: 1.1;
    color: var(--brand-deep);
  }
  .tagline {
    margin-top: 22px; font-family: "Libre Baskerville", Georgia, serif; font-style: italic;
    font-size: 27px; color: var(--ink);
  }
  .rule { position: absolute; top: 222px; left: 179px; width: 841px; height: 2px; background: var(--ink); }

  .panel {
    position: absolute; left: 178px; width: 841px;
    border: 3px solid var(--line); border-radius: 28px;
    background: linear-gradient(180deg, var(--panel-light), var(--panel));
  }
  .panel-title {
    position: absolute; left: 40px; top: 22px;
    font-size: 20px; font-weight: 700; letter-spacing: 0.3px; color: var(--ink);
  }

  .overview { top: 278px; height: 141px; }
  .overview .panel-title { left: 164px; top: 26px; }
  .overview-visual {
    position: absolute; left: 30px; top: 22px; width: 100px; height: 94px; border-radius: 14px;
    background: radial-gradient(circle at 50% 60%, var(--amber), var(--peach) 75%);
  }
  .overview-text { position: absolute; left: 164px; top: 62px; font-size: 19px; line-height: 1.3; color: var(--ink-soft); }
  .applications {
    position: absolute; left: 500px; top: 22px; width: 305px; height: 94px; border-radius: 10px;
    background: linear-gradient(90deg, rgba(240,145,44,0.18), rgba(238,115,37,0.28));
  }

  .features { top: 445px; height: 147px; }
  .feature-badge {
    position: absolute; top: 52px; width: 80px; height: 80px; border-radius: 50%;
    border: 4px solid var(--brand-deep);
    background: radial-gradient(circle, var(--panel-light) 55%, var(--peach));
    display: flex; align-items: center; justify-content: center; text-align: center;
    font-size: 8.5px; font-weight: 700; line-height: 1.15; color: var(--ink-soft); text-transform: uppercase;
  }
  .feature-badge.visual { background: radial-gradient(circle, var(--peach-soft), var(--amber)); }

  .pain-points { top: 621px; height: 147px; }
  .pain-item { position: absolute; top: 90px; font-size: 17.5px; color: var(--ink); }
  .pain-badge {
    position: absolute; left: 34px; top: 52px; width: 80px; height: 80px; border-radius: 50%;
    border: 4px solid var(--brand-deep);
    background: radial-gradient(circle, var(--peach-soft), var(--amber));
  }
  .pain-mark {
    position: absolute; top: 36px; width: 36px; height: 36px; border-radius: 50%;
    background: radial-gradient(circle, var(--peach), var(--peach-soft));
  }

  .performance { top: 795px; height: 152px; }
  .stat-big { position: absolute; left: 40px; top: 64px; font-size: 26px; font-weight: 700; color: var(--brand-deep); }
  .stat-big-label { position: absolute; left: 40px; top: 98px; font-size: 14px; color: var(--ink-soft); }
  .stat-arrow { position: absolute; left: 120px; top: 72px; width: 28px; height: 16px; }
  .stat-list { position: absolute; left: 164px; top: 64px; font-size: 14.5px; line-height: 1.45; color: var(--ink-soft); }
  .stat-list .strong { font-weight: 600; font-size: 16px; }
  .chart { position: absolute; left: 564px; top: 16px; width: 176px; height: 86px; }
  .proof-pill {
    position: absolute; left: 562px; top: 114px; width: 238px; height: 28px; border-radius: 6px;
    background: var(--pill); color: #fff; font-size: 13.5px; font-weight: 700; letter-spacing: 0.3px;
    display: flex; align-items: center; justify-content: center;
  }

  .launch { top: 975px; height: 144px; }
  .calendar { position: absolute; left: 44px; top: 58px; width: 64px; height: 66px; }
  .launch-text { position: absolute; left: 148px; top: 56px; font-size: 18.5px; line-height: 1.32; color: var(--ink); }
  .launch-link { text-decoration: underline; color: var(--ink); }
</style>
</head>
<body>
  <header class="masthead">
    <h1 class="brand-name">Calvero by Moltek</h1>
    <p class="tagline">bold work, bright build, pure Calvero</p>
  </header>
  <div class="rule"></div>

  <section class="panel overview">
    <div class="overview-visual" role="img" aria-label="Adhesive droplet over a tile surface"></div>
    <h2 class="panel-title">PRODUCT OVERVIEW</h2>
    <p class="overview-text">Revolutionary indoor/outdoor<br>adhesive for all surfaces.</p>
    <div class="applications" role="img" aria-label="Kitchens, showers, pools and wall panels where the adhesive is used"></div>
  </section>

  <section class="panel features">
    <h2 class="panel-title">CORE FEATURES</h2>
    <div class="feature-badge visual" style="left:36px" role="img" aria-label="UV stability"></div>
    <div class="feature-badge visual" style="left:191px" role="img" aria-label="Works on all substrates"></div>
    <div class="feature-badge" style="left:314px">Extreme<br>bond<br>strength</div>
    <div class="feature-badge visual" style="left:437px" role="img" aria-label="Trowel application"></div>
    <div class="feature-badge" style="left:564px">Effortless<br>application</div>
    <div class="feature-badge" style="left:699px">Perfect<br>color<br>match</div>
  </section>

  <section class="panel pain-points">
    <h2 class="panel-title">PAIN POINTS SOLVED</h2>
    <div class="pain-badge" role="img" aria-label="Cracked grout"></div>
    <p class="pain-item" style="left:127px">No more cracked grout.</p>
    <div class="pain-mark" style="left:440px" role="img" aria-label="Fading resistance"></div>
    <p class="pain-item" style="left:347px">Resists yellowing/fading.</p>
    <div class="pain-mark" style="left:684px" role="img" aria-label="Installation tool"></div>
    <p class="pain-item" style="left:605px">Simplifies installation.</p>
  </section>

  <section class="panel performance">
    <h2 class="panel-title">PERFORMANCE HIGHLIGHTS</h2>
    <p class="stat-big">500%</p>
    <svg class="stat-arrow" viewBox="0 0 28 16" aria-hidden="true"><path d="M2 8h22M18 3l6 5-6 5" fill="none" stroke="#c2621f" stroke-width="2"/></svg>
    <p class="stat-big-label">Stronger Bond</p>
    <p class="stat-list">2X Faster Cure Time<br><span class="strong">Lifetime UV Guarantee</span></p>
    <svg class="chart" viewBox="0 0 176 86" aria-hidden="true">
      <rect x="4" y="56" width="32" height="30" fill="#f0912c"/>
      <rect x="50" y="39" width="32" height="47" fill="#e07a2a"/>
      <rect x="96" y="19" width="32" height="67" fill="#c2621f"/>
      <rect x="142" y="4" width="32" height="82" fill="#a9501a"/>
      <rect x="0" y="84" width="176" height="2" fill="#a9501a"/>
    </svg>
    <div class="proof-pill">TESTED. PROVEN. UNMATCHED</div>
  </section>

  <section class="panel launch">
    <h2 class="panel-title">LAUNCH &amp; AVAILABILITY</h2>
    <svg class="calendar" viewBox="0 0 64 66" aria-hidden="true">
      <rect x="3" y="8" width="58" height="55" rx="6" fill="#fbe8d2" stroke="#c2621f" stroke-width="3"/>
      <rect x="3" y="8" width="58" height="14" rx="6" fill="#c2621f"/>
      <rect x="15" y="2" width="5" height="12" rx="2" fill="#a9501a"/>
      <rect x="44" y="2" width="5" height="12" rx="2" fill="#a9501a"/>
      <text x="32" y="50" text-anchor="middle" font-family="Montserrat, Arial, sans-serif" font-weight="700" font-size="15" fill="#a9501a">JAN</text>
    </svg>
    <p class="launch-text">Launching January 2024 at Stoneworks Expo.<br>Visit Booth #1234.<br><span class="launch-link">Moltekbond.com/Calvero</span></p>
  </section>
</body>
</html>
```